Business Card Design Project

Looking for a business card that our customers will remember. We are a high end Travel Agency.
Need a re-memorable classy business card.
Both sides full color.
Must have the following details.
Voyage Harbor Logo (see attached)
4B Wattle Lane
Penhurst Sydney NSW 2241
Phone: 02 9471 3652
Fax: 02 9563 4417
sales@voyageharbor-example.com.au
Consultant Name
Anything else you think we need

```html
<!DOCTYPE html>
<html lang="en">
<head>
<meta charset="utf-8">
<title>Voyage Harbor — Business Card</title>
<link rel="stylesheet" href="https://fonts.googleapis.com/css2?family=Open+Sans:wght@300;400&display=swap">
<style>
  :root {
    --backdrop: #444444;
    --card-edge: #3a43a2;
    --band-light: #7090d6;
    --band-mid: #2c4597;
    --band-navy: #232650;
    --band-blue: #3b45a9;
    --rule: #e8ecff;
    --back-core: #6d86d6;
    --back-edge: #3440a0;
    --box-pale: #7e98db;
    --box-blue: #3646a8;
    --box-navy: #222556;
    --ink-light: #f2f4ff;
    --ink-dark: #161a3a;
    --accent: #f2c200;
  }
  * { box-sizing: border-box; margin: 0; padding: 0; }
  html, body { width: 1200px; height: 900px; overflow: hidden; }
  body {
    background: var(--backdrop);
    font-family: "Open Sans", Arial, sans-serif;
    position: relative;
  }
  .card {
    position: absolute;
    width: 560px;
    height: 320px;
    overflow: hidden;
    box-shadow: 0 6px 18px rgba(0,0,0,.35);
  }
  /* Front */
  .card-front { left: 330px; top: 100px; background: var(--card-edge); }
  .band { position: absolute; left: 10px; right: 10px; }
  .band-light { background: var(--band-light); border-top: 2px solid var(--rule); border-bottom: 2px solid var(--rule); }
  .band-top { top: 22px; height: 60px; }
  .band-mid { top: 86px; height: 30px; background: var(--band-mid); }
  .band-navy {
    top: 120px; height: 86px; background: var(--band-navy);
    border-top: 2px solid var(--rule); border-bottom: 2px solid var(--rule);
    display: flex; align-items: center; justify-content: center; gap: 10px;
  }
  .band-blue { top: 210px; height: 34px; background: var(--band-blue); }
  .band-bottom { top: 248px; height: 58px; }
  .brand-name {
    font-weight: 400; font-size: 20px; letter-spacing: 2px;
    color: var(--ink-light); text-transform: uppercase;
  }
  .brand-dot { width: 10px; height: 10px; border-radius: 50%; background: var(--accent); }

  /* Back */
  .card-back {
    left: 590px; top: 470px;
    background: radial-gradient(ellipse at 68% 72%, var(--back-core) 0%, var(--back-edge) 75%);
  }
  .contact-list { position: absolute; left: 8px; top: 14px; display: flex; flex-direction: column; gap: 4px; }
  .contact {
    border: 1px solid var(--rule);
    color: var(--ink-light);
    font-weight: 300;
    display: flex; flex-direction: column; justify-content: center;
    padding: 0 8px; height: 50px;
  }
  .contact-address { width: 290px; background: var(--box-pale); font-size: 15px; line-height: 1.15; }
  .contact-email { width: 280px; background: var(--box-blue); font-size: 15px; }
  .contact-web { width: 280px; background: var(--box-navy); font-size: 14px; padding-left: 16px; }
  .contact-fax { width: 186px; background: var(--box-blue); font-size: 17px; }
  .contact-phone { width: 205px; background: var(--box-blue); font-size: 17px; }
  .back-brand {
    position: absolute; left: 310px; top: 150px;
    display: flex; align-items: center; gap: 10px;
  }
  .back-brand .brand-name { color: var(--ink-dark); font-size: 19px; }
  .back-brand .brand-dot { background: var(--ink-dark); }
</style>
</head>
<body>
  <section class="card card-front" aria-label="Business card front">
    <div class="band band-light band-top"></div>
    <div class="band band-mid"></div>
    <div class="band band-navy">
      <span class="brand-name">Voyage Harbor</span>
      <span class="brand-dot"></span>
    </div>
    <div class="band band-blue"></div>
    <div class="band band-light band-bottom"></div>
  </section>

  <section class="card card-back" aria-label="Business card back">
    <div class="contact-list">
      <div class="contact contact-address"><span>4B Wattle Lane</span><span>Penhurst Sydney NSW 2241</span></div>
      <div class="contact contact-email">sales@voyageharbor-example.com.au</div>
      <div class="contact contact-web">www.voyageharbor-example.com.au</div>
      <div class="contact contact-fax">Fax: 02 9563 4417</div>
      <div class="contact contact-phone">Phone: 02 9471 3652</div>
    </div>
    <div class="back-brand">
      <span class="brand-name">Voyage Harbor</span>
      <span class="brand-dot"></span>
    </div>
  </section>
</body>
</html>
```